My company is throwing a party. The name is 70/30 (70% Reggae & 30% Whatever Comes)

I seek a flyer that shows this will be a very elegant, upscale event and at the same time high energy, great reggae music and dancing.

I need this flyer to be 650 pixels wide & any length, High resolution (1MB) for printing on a 4" x 6" flyer.

Target Market(s)

Fans of reggae music

Industry/Entity Type

Printing

Requirements
Must have
• Lumen Harbor Holdings Presents:
70/30
Upscale Reggae Soiree
70% Reggae - 30% Whatever Comes

Saturday May 4th, 10pm - 3am

The Copperloft: 418 1/2 North Callow St, OKC

Dress to impress! We reserve the right to refuse entry

Free Entry: 1st 50 Ladies On VIP Guestlist - Discounted Early Bird Online Tickets - For Bottle Service Reservation: http://islandnights.ticketvoro.com

More info? 405-617-2958

```html
<!DOCTYPE html>
<html lang="en">
<head>
<meta charset="utf-8">
<title>70/30 — Upscale Reggae Soiree</title>
<link href="https://fonts.googleapis.com/css2?family=Archivo+Black&family=Montserrat:wght@500;600&family=Russo+One&display=swap" rel="stylesheet">
<style>
  :root {
    --rasta-red: #e5161c;
    --rasta-gold: #f6d20a;
    --rasta-green: #3fd11a;
    --ink: #0b0b0b;
    --white: #ffffff;
    --date-red: #ee1c24;
    --band-yellow: #fff200;
  }
  html, body {
    margin: 0;
    padding: 0;
    width: 1200px;
    height: 2702px;
    overflow: hidden;
    background: #ffffff;
  }
  .flyer {
    position: relative;
    width: 1200px;
    height: 2702px;
    overflow: hidden;
    background:
      radial-gradient(ellipse 520px 700px at 600px 1800px, rgba(246,210,10,0.95), rgba(246,210,10,0) 70%),
      linear-gradient(90deg, var(--rasta-red) 0%, #ef4a14 30%, var(--rasta-gold) 52%, #9fe014 68%, var(--rasta-green) 100%);
  }
  .portrait-art {
    position: absolute;
    left: 360px;
    top: 0;
    width: 840px;
    height: 1180px;
    background: radial-gradient(ellipse 380px 520px at 470px 440px, rgba(10,10,10,0.92) 0%, rgba(10,10,10,0.75) 55%, rgba(10,10,10,0) 80%);
  }
  .record-art {
    position: absolute;
    left: 330px;
    top: 1430px;
    width: 560px;
    height: 560px;
    border-radius: 50%;
    background: radial-gradient(circle, #f7a51c 0%, #f4c21b 20%, #e9b40f 45%, rgba(240,200,20,0.3) 70%, rgba(240,200,20,0) 100%);
  }
  .guitar-art {
    position: absolute;
    left: 980px;
    top: 1300px;
    width: 220px;
    height: 960px;
    background: linear-gradient(200deg, rgba(30,150,20,0.55), rgba(30,150,20,0));
  }
  .presenter {
    position: absolute;
    top: 96px;
    left: 0;
    width: 1200px;
    text-align: center;
    font-family: "Montserrat", sans-serif;
    font-weight: 500;
    font-size: 58px;
    line-height: 1.05;
    color: var(--white);
    text-shadow: 0 0 4px rgba(0,0,0,0.6);
    margin: 0;
  }
  .subtitle {
    position: absolute;
    top: 236px;
    left: 0;
    width: 1200px;
    text-align: center;
    font-family: "Montserrat", sans-serif;
    font-weight: 600;
    font-size: 40px;
    letter-spacing: 4px;
    color: var(--white);
    text-shadow: 0 0 4px rgba(0,0,0,0.6);
    margin: 0;
  }
  .headline-art {
    position: absolute;
    left: 0;
    top: 0;
    width: 1200px;
    height: 2702px;
  }
  .event-name {
    font-family: "Russo One", sans-serif;
    font-size: 600px;
    fill: var(--white);
  }
  .tagline-main, .tagline-sub {
    font-family: "Archivo Black", sans-serif;
    fill: var(--ink);
  }
  .tagline-main { font-size: 140px; }
  .tagline-sub { font-size: 112px; }
  .date-block {
    position: absolute;
    left: 590px;
    top: 1485px;
    width: 470px;
    margin: 0;
    font-family: "Archivo Black", sans-serif;
    font-size: 78px;
    line-height: 0.98;
    color: var(--date-red);
    text-align: center;
    transform: rotate(-4deg);
    -webkit-text-stroke: 3px var(--white);
    paint-order: stroke fill;
  }
  .info {
    position: absolute;
    left: 175px;
    top: 1766px;
    width: 900px;
    font-family: "Archivo Black", sans-serif;
    font-size: 40px;
    line-height: 1.05;
    color: var(--white);
    text-shadow: 3px 3px 0 var(--ink), -1px -1px 0 var(--ink), 1px -1px 0 var(--ink), -1px 1px 0 var(--ink);
    transform: rotate(4deg);
    transform-origin: left top;
  }
  .info p { margin: 0 0 60px 0; }
  .contact-band {
    position: absolute;
    left: 90px;
    top: 2565px;
    width: 1025px;
    height: 120px;
    background: linear-gradient(90deg, #f3ea18, var(--band-yellow) 50%, #e8f010);
    display: flex;
    align-items: center;
    justify-content: center;
    gap: 20px;
    font-family: "Archivo Black", sans-serif;
    font-size: 66px;
  }
  .contact-band .label { color: var(--date-red); }
  .contact-band .phone { color: var(--ink); }
</style>
</head>
<body>
  <main class="flyer">
    <div class="portrait-art" role="img" aria-label="Stylised portrait of a reggae singer with dreadlocks in red, green and black"></div>
    <div class="record-art" role="img" aria-label="Spinning vinyl record in gold tones"></div>
    <div class="guitar-art" role="img" aria-label="Electric guitar silhouette in green"></div>

    <p class="presenter">LUMEN HARBOR HOLDINGS<br>PRESENTS</p>
    <p class="subtitle">UPSCALE REGGAE SOIREE</p>

    <svg class="headline-art" viewBox="0 0 1200 2702" aria-labelledby="eventTitle">
      <title id="eventTitle">70/30 — 70% Reggae, 30% Whatever Comes</title>
      <g transform="rotate(-3 600 830)">
        <text class="event-name" x="90" y="1060" textLength="1010" lengthAdjust="spacingAndGlyphs" transform="translate(0 -212) scale(1 1.2)">70/30</text>
      </g>
      <g transform="rotate(-8 600 1300)">
        <text class="tagline-main" x="200" y="1275" textLength="860" lengthAdjust="spacingAndGlyphs">70% Reggae</text>
        <text class="tagline-sub" x="135" y="1405" textLength="890" lengthAdjust="spacingAndGlyphs">30% Whatever Comes</text>
      </g>
    </svg>

    <p class="date-block">Saturday<br>May 4th<br>10pm - 3am</p>

    <section class="info">
      <p>The Copperloft:<br>418 1/2 North Callow St, OKC</p>
      <p>Dress to impress!<br>We reserve the right to refuse<br>entry</p>
      <p>Free Entry: 1st 50 Ladies On VIP<br>Guestlist - Discounted Early Bird</p>
      <p>Online Tickets - For Bottle<br>Service Reservation:<br>http://islandnights.ticketvoro.com</p>
    </section>

    <div class="contact-band">
      <span class="label">More info?</span>
      <span class="phone">405-617-2958</span>
    </div>
  </main>
</body>
</html>
```